For Creative Minds: A Simple Clean Book Cover that Stands Out

This will be a christian book teaching christians about divine healing. It is part of a series called "Morning Step Collection". I want the book cover to communicate the idea of healing, and specifically heavenly healing from God. These are some of the specifications below

1. General
Book to be published on print harbor platform
Dimensions: 6 x 9 inches, Paperback
Number of words: Estimated to be about 60,000 words.
Please use Indesign for design and submit the final Indesign source files along with the final design.

2. Cover image.
Image can be either human or any object that can communicate the idea above. No human faces to show up prominently.
High quality image is highly solicited.

3. Title:
" Forty Evenings Toward Lasting Renewal Within Your Soul"

3. Author name
Preferably should appear below. Open to creative ideas with titles that are better placed above.

Author's Name: Duncan Ferrow

3. Layout
Should not be too busy.
Simple and clean layout appeals more to me.

4. Series name
AS noted above, this book will be part of a series called " Morning Step Collection". I want this series name to appear somewhere in the cover and to have a simple but unique design that will be used for all subsequent titles. The Title of the book should have the emphasis.

I have attached a sample cover for one of my monthly devotional books which I choose from a contest.

ABOUT THE AUTHOR
Duncan Ferrow represents the blessed combination of Physician and Minister, bringing healing not only to the physical body but to the spiritual heart. He currently works as the Director of the Hospital Medicine Program at the Bellhaven County Care Campus in Iowa, USA. He is the Founder of Lantern & Vine Fellowship, a teaching ministry that seeks to bring believers into the fullness of grace — the glory of God — through conferences, seminars and books.

One of his notable quotes is “The Word of God is the most potent and efficient remedy for all the ailments of humanity.” This clearly portrays his experience with the Word as a Physician who is familiar with the powers, both natural and supernatural, to mend broken human beings. 

He currently lives in Iowa, USA with his wife, Lu Tessin, and daughter, Rosalind. You can reach out to Patrick using the contact information listed below.

BLURB
As a Physician and Minister, I have seen the power of modern medicine to bring about healing in the body and mind as well as the operation of the power of God to produce amazing medical results. However, many people are just not aware of the reality of divine healing. To some, it is a myth, belief or some "faith talk" in the heart. Medical miracles are real and we should take full advantage of it. As much as a love being a physician and treat patients in the hospital, I have come to see both its amazing successes and many limitations.

Industry/Entity Type

Christian

Font styles to use
Serif

Colors

Designer to choose colors to be used in the design.

Requirements
Should not have
• Too stylistic fonts

```html
<!DOCTYPE html>
<html lang="en">
<head>
<meta charset="utf-8">
<title>Forty Evenings Toward Lasting Renewal Within Your Soul — Cover Wrap</title>
<link rel="stylesheet" href="https://fonts.googleapis.com/css2?family=Crimson+Text:wght@400;600&display=swap">
<style>
  :root {
    --white: #ffffff;
    --sky-top: #3d8fe0;
    --sky-mid: #2a64bf;
    --navy-deep: #141d4f;
    --navy-ink: #1c2157;
    --night: #0d1236;
    --series-violet: #a04fc0;
    --cloud: #dbe9f8;
    --field: #4a3a6a;
  }
  * { margin: 0; padding: 0; box-sizing: border-box; }
  html, body { width: 1200px; height: 864px; overflow: hidden; background: #ffffff; }
  .cover-wrap {
    position: relative; width: 1200px; height: 864px; overflow: hidden;
    font-family: "Crimson Text", Georgia, serif; color: var(--white);
  }

  /* Back cover */
  .back-cover {
    position: absolute; left: 0; top: 0; width: 560px; height: 864px;
    background: linear-gradient(180deg, var(--sky-top) 0%, var(--sky-mid) 30%, #203f98 55%, var(--navy-deep) 85%, var(--night) 100%);
  }
  .back-title { position: absolute; left: 0; top: 38px; width: 590px; text-align: center; text-transform: uppercase; line-height: 1; font-weight: 400; }
  .back-title .line-lead { display: block; font-size: 56px; }
  .back-title .line-mid { display: block; font-size: 27px; margin-top: 6px; }
  .back-title .line-main { display: block; font-size: 46px; margin-top: 6px; }
  .back-intro {
    position: absolute; left: 58px; top: 186px; width: 474px;
    font-size: 15px; line-height: 19px; text-align: center;
  }
  .back-divider {
    position: absolute; left: 110px; top: 370px; width: 370px; height: 2px;
    background: linear-gradient(90deg, transparent, rgba(255,255,255,.85), transparent);
  }
  .author-photo-slot {
    position: absolute; left: 47px; top: 398px; width: 171px; height: 214px; background: var(--white);
  }
  .author-bio {
    position: absolute; left: 234px; top: 396px; width: 300px;
    font-size: 15px; line-height: 19px; text-align: left;
  }

  /* Spine */
  .spine {
    position: absolute; left: 560px; top: 0; width: 64px; height: 864px; overflow: hidden;
    background: linear-gradient(180deg, #3384d8 0%, #2457b2 35%, #1b2f7c 70%, var(--night) 100%);
  }
  .spine-text {
    position: absolute; left: 50%; transform: translateX(-50%);
    writing-mode: vertical-rl; text-transform: uppercase; white-space: nowrap; line-height: 1;
  }
  .spine-title { top: 42px; font-size: 17.5px; letter-spacing: .1px; }
  .spine-author { top: 652px; font-size: 23px; }

  /* Front cover */
  .front-cover { position: absolute; left: 624px; top: 0; width: 576px; height: 864px; overflow: hidden; }
  .front-art {
    position: absolute; inset: 0;
    background:
      radial-gradient(ellipse 55% 40% at 45% 38%, rgba(255,255,255,.75), transparent 70%),
      linear-gradient(180deg, #2f86d6 0%, #6aaee6 25%, var(--cloud) 50%, #b8c8e4 64%, #6c5a86 74%, var(--field) 84%, #1f1840 100%);
  }
  .front-title { position: absolute; left: 0; top: 122px; width: 576px; text-align: center; text-transform: uppercase; line-height: 1; font-weight: 400; }
  .front-title span { display: block; }
  .front-title .t-lead { font-size: 60px; color: var(--white); }
  .front-title .t-sub { font-size: 38px; color: var(--white); margin-top: 12px; }
  .front-title .t-sub-ink { font-size: 38px; color: var(--navy-ink); margin-top: 4px; }
  .front-title .t-main { font-size: 74px; color: var(--navy-ink); margin-top: 4px; }
  .series-mark {
    position: absolute; left: 0; top: 747px; width: 576px; text-align: center;
    font-size: 15px; color: var(--series-violet); text-transform: uppercase; letter-spacing: .3px;
  }
  .series-mark span { border-bottom: 1px solid var(--series-violet); padding-bottom: 2px; }
  .front-author {
    position: absolute; left: 0; top: 778px; width: 576px; text-align: center;
    font-size: 44px; text-transform: uppercase; color: var(--white);
  }
</style>
</head>
<body>
<main class="cover-wrap">
  <section class="back-cover">
    <h2 class="back-title">
      <span class="line-lead">Forty Evenings</span>
      <span class="line-mid">Toward Lasting Renewal Within</span>
      <span class="line-main">Your Soul</span>
    </h2>
    <p class="back-intro">Lorem Ipsum is simply dummy text of the printing and typesetting industry. Lorem Ipsum has been the industry's standard dummy text ever since the 1500s, when an unknown printer took a galley of type and scrambled it to make a type specimen book. It has survived not only five centuries, but also the leap into electronic typesetting, remaining essentially unchanged. It was popularised in the 1960s with the release of Markwell sheets containing Lorem Ipsum passages, and more recently with desktop publishing software like Quillset Composer including versions of Lorem Ipsum.</p>
    <div class="back-divider"></div>
    <div class="author-photo-slot" role="img" aria-label="Author portrait placeholder"></div>
    <p class="author-bio">Lorem Ipsum is simply dummy text of the printing and typesetting industry. Lorem Ipsum has been the industry's standard dummy text ever since the 1500s, when an unknown printer took a galley of type and scrambled it to make a type specimen book. It has survived not only five centuries, but also the leap into electronic typesetting, remaining essentially unchanged. It was popularised in the 1960s with the release of Markwell sheets containing Lorem Ipsum passages, and more recently with desktop publishing software like Quillset Composer including versions of Lorem Ipsum.</p>
  </section>

  <section class="spine">
    <span class="spine-text spine-title">Forty Evenings Toward Lasting Renewal Within Your Soul</span>
    <span class="spine-text spine-author">Duncan Ferrow</span>
  </section>

  <section class="front-cover">
    <div class="front-art" role="img" aria-label="Photograph of a person with arms outstretched in a grassy field beneath a bright sky of clouds and flying gulls"></div>
    <h1 class="front-title">
      <span class="t-lead">Forty Evenings</span>
      <span class="t-sub">Toward Lasting</span>
      <span class="t-sub-ink">Renewal Within</span>
      <span class="t-main">Your Soul</span>
    </h1>
    <p class="series-mark"><span>Morning Step Collection</span></p>
    <p class="front-author">Duncan Ferrow</p>
  </section>
</main>
</body>
</html>
```